BSC Flyer to attract applicants 11x17

Brightline Stagecraft Company provides crew for local concerts, filming, theater, and corporate events.
The flyer will be posted on bulletin boards at colleges with theater programs.
Our primary venues are historic theaters in downtown LA
Need a 11x17 poster to attract potential applicants/crew
I have attached a poster that one of our staff made that has all if the relevant info - but i know the poster can look much better than that. I have also attached many images and our logo. It is not necessary to use all of the images, or any of them. The two images of the theater interiors are the venues we operate so they would be the first to include. I can send additional info or images upon request. Thank you

Entertainment

• APPLY@BSCCREWHUB.LA

```html
<!DOCTYPE html>
<html lang="en">
<head>
<meta charset="utf-8">
<title>Brightline Stagecraft Company – Open Positions</title>
<link rel="stylesheet" href="https://fonts.googleapis.com/css2?family=Poppins:ital,wght@0,800;0,900;1,600;1,800&display=swap">
<style>
  :root {
    --page-bg: #ebebed;
    --brand-blue: #0b4fc4;
    --deep-blue: #0a2fb8;
    --sky-blue: #2f6fe0;
    --white: #ffffff;
    --night: #1d1f24;
    --smoke: #3b3d42;
    --icon-navy: #0a2a6a;
  }
  * { margin: 0; padding: 0; box-sizing: border-box; }
  html, body { width: 1200px; height: 997px; overflow: hidden; background: var(--page-bg); }

  .flyer {
    position: absolute; left: 331px; top: 66px;
    width: 563px; height: 869px; overflow: hidden;
    background: linear-gradient(180deg, var(--smoke) 45%, var(--night) 100%);
    box-shadow: 0 10px 30px rgba(0,0,0,.35);
    font-family: "Poppins", sans-serif;
  }
  .top-band { position: absolute; left: 0; top: 0; width: 100%; height: 33px; background: var(--deep-blue); }

  .masthead {
    position: absolute; left: 0; top: 33px; width: 100%; height: 77px;
    background: var(--white);
    display: flex; align-items: center; justify-content: center;
  }
  .masthead-name {
    font-size: 25px; font-weight: 800; color: var(--brand-blue);
    letter-spacing: 0.5px; line-height: 1;
  }

  .city-backdrop {
    position: absolute; left: 0; top: 110px; width: 100%; height: 340px;
    background: linear-gradient(180deg, var(--deep-blue) 0%, var(--sky-blue) 50%, #2b3a66 82%, var(--smoke) 100%);
  }

  .photo-grid {
    position: absolute; left: 34px; top: 138px; width: 297px; height: 297px;
    border: 3px solid var(--white); border-radius: 20px; overflow: hidden;
    display: grid; grid-template-columns: 1fr 1fr; grid-template-rows: 1fr 1fr; gap: 5px;
    background: var(--white);
  }
  .photo { width: 100%; height: 100%; }
  .photo-rigging { background: linear-gradient(135deg, #5a3fe0, #9a8cf2 55%, #3a2aa0); }
  .photo-console { background: linear-gradient(160deg, #6f7480, #c9c3b4 45%, #3a3d44); }
  .photo-theater { background: radial-gradient(ellipse at 50% 15%, #c9a0ff 0%, #b5602c 30%, #5b2a1a 75%, #2a1822 100%); }
  .photo-singer  { background: radial-gradient(ellipse at 50% 30%, #e8eefc 0%, #4a6fd8 35%, #0d1640 80%); }

  .brand-mark {
    position: absolute; left: 354px; top: 198px; width: 171px; height: 177px;
    display: flex; align-items: center; justify-content: center; gap: 8px;
  }
  .brand-mark .dot { width: 24px; height: 24px; border-radius: 50%; background: var(--white); }
  .brand-mark .name { font-size: 56px; font-weight: 900; color: var(--white); line-height: 1; }

  .diagonal-band { position: absolute; left: 0; top: 0; width: 563px; height: 869px; }

  .headline {
    position: absolute; left: 0; width: 100%; text-align: center;
    font-weight: 900; color: var(--brand-blue); line-height: 1;
    text-shadow: 0 0 2px var(--white), 0 3px 6px rgba(0,0,0,.45);
  }
  .headline-1 { top: 455px; font-size: 84px; letter-spacing: 2px; }
  .headline-2 { top: 523px; font-size: 82px; }

  .tagline {
    position: absolute; left: 81px; top: 610px; width: 400px;
    transform: rotate(-4deg); transform-origin: center;
    color: var(--white); font-style: italic; font-weight: 600; font-size: 26px;
    letter-spacing: 10px; line-height: 1.05; text-align: center;
  }

  .role-box {
    position: absolute; left: 56px; top: 688px; width: 364px; height: 74px;
    background: var(--brand-blue); padding: 3px 0 0 12px;
    color: var(--white); font-style: italic; font-weight: 800; font-size: 22px; line-height: 1.04;
  }
  .role-icon { position: absolute; left: 433px; top: 688px; width: 69px; height: 74px; background: var(--brand-blue); }
  .role-icon .figure { position: absolute; left: 18px; top: 10px; width: 33px; height: 54px; background: var(--icon-navy); border-radius: 4px; }

  .apply-label {
    position: absolute; right: 63px; top: 781px;
    color: var(--white); font-style: italic; font-weight: 800; font-size: 16px; letter-spacing: 3px; line-height: 1.2;
  }
  .apply-email {
    position: absolute; right: 59px; top: 802px; height: 22px;
    background: var(--brand-blue); color: var(--white);
    font-style: italic; font-weight: 600; font-size: 15px; letter-spacing: 1.5px; line-height: 22px; padding: 0 6px;
  }
  .website {
    position: absolute; left: 37px; top: 828px;
    color: var(--white); font-style: italic; font-weight: 600; font-size: 12px; letter-spacing: 4px;
  }
</style>
</head>
<body>
  <main class="flyer">
    <div class="top-band"></div>

    <header class="masthead">
      <p class="masthead-name">BRIGHTLINE STAGECRAFT COMPANY</p>
    </header>

    <div class="city-backdrop" role="img" aria-label="Downtown Los Angeles skyline at dusk, tinted blue"></div>

    <div class="photo-grid">
      <div class="photo photo-rigging" role="img" aria-label="Line array speakers rigged above a stage in purple light"></div>
      <div class="photo photo-console" role="img" aria-label="Digital audio mixing console"></div>
      <div class="photo photo-theater" role="img" aria-label="Ornate interior of a historic downtown theater"></div>
      <div class="photo photo-singer" role="img" aria-label="Silhouetted performer on stage under spotlights"></div>
    </div>

    <div class="brand-mark">
      <span class="dot"></span>
      <span class="name">BSC</span>
    </div>

    <svg class="diagonal-band" viewBox="0 0 563 869" aria-hidden="true">
      <polygon points="0,511 563,468 563,543 0,594" fill="#ffffff"/>
    </svg>

    <h1 class="headline headline-1">HAS OPEN</h1>
    <div class="headline headline-2">POSITIONS</div>

    <p class="tagline">WE ARE LOOKING<br>FOR TALENTED</p>

    <p class="role-box">TECHNICIANS TO<br>ADD TO OUR ROSTER<br>OF SKILLED PROFESSIONALS.</p>
    <div class="role-icon" role="img" aria-label="Crew technician icon"><span class="figure"></span></div>

    <p class="apply-label">SEND RESUME TO:</p>
    <p class="apply-email">APPLY@BSCCREWHUB.LA</p>
    <p class="website">WWW.BSCCREWHUB.LA</p>
  </main>
</body>
</html>
```